Very clean, very simple business card needed.

I am looking for a VERY simple business card. I have attached our logo. I would like it to be a mainly white card. I have picked double sided but would be open to single as well. I want the overall feel to be simple, classic, and professional. Thank you.

Industry/Entity Type

Consultant

Contact Information for Business Card

Daniel Fenwick

2870 North 9th Avenue, Summit Floor, Calder Heights, Northvale 60871
dan@belmorevista.com
www.belmorevista.com

Font styles to use
Serif

Colors

Designer to choose colors to be used in the design.

Requirements
Must have
• The business card details and in an editable form to change the names and emails of employees easily.
Nice to have
• n/a
Should not have
• Pictures, big lines and stripes, too much color.

```html
<!DOCTYPE html>
<html lang="en">
<head>
<meta charset="utf-8">
<title>Belmore Vista – Business Card</title>
<link rel="stylesheet" href="https://fonts.googleapis.com/css2?family=Marcellus&family=Open+Sans:wght@400&display=swap">
<style>
  :root {
    --navy: #2a2a86;
    --ink: #4a4a4a;
    --paper: #ffffff;
    --stage: #e9e9ec;
    --faint: #ececef;
  }
  * { margin: 0; padding: 0; box-sizing: border-box; }
  html, body { width: 1200px; height: 800px; overflow: hidden; }
  body {
    background: var(--stage);
    display: flex;
    align-items: center;
    justify-content: center;
    gap: 60px;
  }
  .card {
    position: relative;
    width: 510px;
    height: 292px;
    background: var(--paper);
    box-shadow: 0 2px 10px rgba(0, 0, 0, 0.12);
    overflow: hidden;
  }

  /* Front */
  .card--front {
    display: flex;
    align-items: center;
    justify-content: center;
    gap: 14px;
  }
  .brand-mark {
    width: 24px;
    height: 24px;
    background: var(--navy);
  }
  .brand-name {
    font-family: "Marcellus", serif;
    font-size: 32px;
    letter-spacing: 1px;
    color: var(--navy);
    text-transform: uppercase;
  }

  /* Back */
  .accent-block {
    position: absolute;
    top: 0;
    right: 0;
    width: 180px;
    height: 118px;
    background: var(--faint);
  }
  .person-name {
    position: absolute;
    left: 60px;
    top: 128px;
    font-family: "Marcellus", serif;
    font-weight: 400;
    font-size: 23px;
    color: var(--navy);
    font-variant: small-caps;
    letter-spacing: 0.5px;
  }
  .divider {
    position: absolute;
    left: 290px;
    top: 170px;
    width: 2px;
    height: 44px;
    background: var(--navy);
  }
  .contact-list {
    position: absolute;
    left: 310px;
    top: 170px;
    list-style: none;
    font-family: "Open Sans", sans-serif;
    font-size: 12.5px;
    color: var(--ink);
  }
  .contact-list li {
    display: flex;
    align-items: center;
    gap: 8px;
    height: 22px;
  }
  .icon { width: 16px; height: 16px; flex: none; }
  .address {
    position: absolute;
    left: 34px;
    bottom: 30px;
    display: flex;
    align-items: center;
    gap: 12px;
    font-family: "Open Sans", sans-serif;
    font-style: normal;
    font-size: 12.5px;
    line-height: 1.35;
    color: var(--ink);
  }
</style>
</head>
<body>

  <section class="card card--front" aria-label="Card front">
    <span class="brand-mark"></span>
    <span class="brand-name">Belmore Vista</span>
  </section>

  <section class="card card--back" aria-label="Card back">
    <div class="accent-block"></div>
    <h1 class="person-name">Daniel Fenwick</h1>
    <div class="divider"></div>
    <ul class="contact-list">
      <li>
        <svg class="icon" viewBox="0 0 16 16" aria-hidden="true">
          <circle cx="8" cy="8" r="8" fill="var(--navy)"/>
          <rect x="4" y="5.2" width="8" height="5.6" fill="none" stroke="#fff" stroke-width="1"/>
          <polyline points="4,5.2 8,8.5 12,5.2" fill="none" stroke="#fff" stroke-width="1"/>
        </svg>
        <span class="email">dan@belmorevista.com</span>
      </li>
      <li>
        <svg class="icon" viewBox="0 0 16 16" aria-hidden="true">
          <circle cx="8" cy="8" r="8" fill="var(--navy)"/>
          <circle cx="8" cy="8" r="4.5" fill="none" stroke="#fff" stroke-width="0.9"/>
          <ellipse cx="8" cy="8" rx="2" ry="4.5" fill="none" stroke="#fff" stroke-width="0.9"/>
          <line x1="3.5" y1="8" x2="12.5" y2="8" stroke="#fff" stroke-width="0.9"/>
        </svg>
        <span class="web">www.belmorevista.com</span>
      </li>
    </ul>
    <address class="address">
      <svg class="icon" viewBox="0 0 16 16" aria-hidden="true">
        <circle cx="8" cy="8" r="8" fill="var(--navy)"/>
        <path d="M8 3.6a3 3 0 0 0-3 3c0 2.2 3 5.6 3 5.6s3-3.4 3-5.6a3 3 0 0 0-3-3z" fill="none" stroke="#fff" stroke-width="1"/>
        <circle cx="8" cy="6.6" r="1" fill="#fff"/>
      </svg>
      <span>2870 North 9th Avenue,<br>Summit Floor, Calder Heights,<br>Northvale 60871</span>
    </address>
  </section>

</body>
</html>
```